Corvell Ashdown Website

Updated website for Corvell Ashdown Dry Cleaners & Garment Care.

Please look at www.tindalepressers.example we really like this site!!!

We are not set on colors or fonts. Looking for an professional easy to use site that looks and works even better on a mobile device. 90% of our customers visit us on cell phones.

Target Market(s)

We are located in an up scale area with young trendy individuals but, also very successful mature customers as well. Probably geared more to tech savvy younger crowd.

Industry/Entity Type

Dry Cleaning

Coding

Coded - Design and coding required

Font styles to use
Serif
Script

Colors
85abd2
85cae6
cee9f5
cfdeed
757575

Requirements
Must have
• Must look good on a mobile device and have sign up for our pick up and delivery. Geographical pick up and delivery perimeters would be great as well. Capturing emails and other user data for future marketing. We do a lot of advertising.
• Please look at www.tindalepressers.example we really like this site!!!
• Search engine optimized.
• Also we are adding a new POS system that will have a login for customers and possibly an app.
Nice to have
• 100% satisfaction guaranteed and scrolling reviews somewhere on the page.

```html
<!DOCTYPE html>
<html lang="en">
<head>
<meta charset="utf-8">
<title>Corvell Ashdown Dry Cleaners &amp; Garment Care</title>
<link href="https://fonts.googleapis.com/css2?family=Questrial&display=swap" rel="stylesheet">
<style>
:root{
  --accent:#85cae6;
  --accent-deep:#85abd2;
  --link:#5f9fd3;
  --pale:#cee9f5;
  --mist:#cfdeed;
  --text:#757575;
  --ink:#2f3540;
  --band:#eef2f6;
  --footer:#3c4452;
  --white:#ffffff;
}
*{box-sizing:border-box;margin:0;padding:0}
html,body{width:1200px;height:3364px;overflow:hidden}
body{font-family:"Questrial",sans-serif;color:var(--text);background:var(--white);position:relative}
section,header,footer{position:absolute;left:0;width:1200px;overflow:hidden}
.abs{position:absolute}
.center{left:0;width:1200px;text-align:center}
.btn{position:absolute;display:flex;align-items:center;justify-content:center;background:var(--accent);color:var(--white);font-size:14px;border-radius:2px}
.btn-ghost{position:absolute;display:flex;align-items:center;justify-content:center;border:1px solid var(--pale);color:var(--accent);font-size:13px;background:var(--white)}
.eyebrow{font-size:17px;color:#555}
.heading{font-size:38px;color:var(--ink);font-weight:400}

/* hero */
.hero{top:0;height:640px}
.hero-photo{position:absolute;inset:0;background:linear-gradient(100deg,#4a3a3c 0%,#6f5a5a 30%,#8c7b78 55%,#5d5a5e 80%,#3e3f45 100%)}
.hero-shade{position:absolute;inset:0;background:rgba(20,22,28,.45)}
.brand{display:flex;align-items:center;gap:12px;color:var(--white);font-size:22px}
.brand-dot{width:52px;height:52px;border-radius:50%;background:var(--white);opacity:.9}
.nav{top:44px;left:420px;display:flex;gap:26px;font-size:13px;color:var(--white)}
.nav .active{color:var(--accent)}
.login{top:44px;left:918px;font-size:13px;color:var(--white);display:flex;gap:6px;align-items:center}
.hero-kicker{top:222px;font-size:18px;color:var(--white)}
.hero-title{top:250px;font-size:38px;color:var(--white);font-weight:400}
.zip{left:386px;top:334px;width:426px;height:36px;display:flex;background:rgba(255,255,255,.92)}
.zip span{flex:1;font-size:11px;color:#999;padding:12px 10px}
.zip b{width:114px;background:var(--accent-deep);color:var(--white);font-weight:400;font-size:12px;display:flex;align-items:center;justify-content:center}
.hero-note{top:398px;font-size:18px;color:var(--white)}
.app-badge{top:466px;width:184px;height:50px;border-radius:5px;background:#111;border:1px solid #888}

/* why */
.why{top:640px;height:460px}
.feature{position:absolute;top:188px;width:300px;text-align:center}
.feature-icon{margin:0 auto;width:96px;height:96px;border-radius:50%;border:2px solid var(--pale);display:flex;align-items:center;justify-content:center}
.feature-icon.on{background:var(--accent);border-color:var(--pale)}
.feature p{margin-top:18px;font-size:17px;color:#555}
.feature p.linked{color:#444;text-decoration:underline}

/* about */
.about{top:1100px;height:366px;background:var(--band)}
.about-photo{left:689px;top:0;width:356px;height:366px;background:linear-gradient(160deg,#e9e6e4 0%,#c9c3c6 30%,#4a5b8a 55%,#b43a45 75%,#d18ac1 100%)}
.about-text{left:157px;top:240px;width:490px;font-size:13px;line-height:20px;color:#555}

/* services */
.services{top:1466px;height:571px}
.service{position:absolute;top:180px;width:204px;text-align:center}
.service-photo{width:204px;height:200px}
.service p{margin-top:14px;font-size:17px;color:#444}
.service p.linked{color:var(--link);text-decoration:underline}
.arrow{position:absolute;font-size:22px;color:#444}

/* guarantee */
.guarantee{top:2037px;height:359px}
.guarantee-photo{position:absolute;inset:0;background:linear-gradient(90deg,#f3f1ec 0%,#e6e6e2 40%,#c9d6df 60%,#b8a07a 78%,#8a9ea8 100%)}
.guarantee-title{left:157px;top:112px;font-size:34px;color:var(--ink)}
.guarantee-title em{color:var(--accent-deep);font-style:italic}
.guarantee-text{left:157px;top:192px;width:560px;font-size:17px;line-height:28px;color:#333}

/* testimonials */
.testimonials{top:2396px;height:514px}
.quote{position:absolute;top:190px;width:250px}
.avatar{width:88px;height:88px;border-radius:50%;border:3px solid var(--pale);background:radial-gradient(circle,#d8cfc8 0%,#b9aca4 70%)}
.quote p{margin-top:32px;font-size:12px;line-height:20px;color:#666}
.quote .who{margin-top:14px;font-size:13px;color:var(--link);text-decoration:underline;line-height:16px}
.quote .role{font-size:12px;color:#888}

/* footer */
.site-footer{top:2910px;height:454px;background:var(--footer);color:#cfd5dd}
.footer-col{position:absolute;top:102px;font-size:12px;line-height:22.4px}
.footer-col h4{font-size:16px;font-weight:400;color:var(--white);margin-bottom:28px}
.footer-col .current{color:var(--accent)}
.social{position:absolute;left:1003px;width:40px;height:40px;border-radius:50%;border:1px solid #aab3c0}
.social.on{background:var(--accent-deep);border-color:var(--accent-deep)}
.rule{left:157px;top:372px;width:886px;height:1px;background:#566072}
</style>
</head>
<body>

<header class="hero">
  <div class="hero-photo" role="img" aria-label="Rack of colourful shirts and dresses hanging in a boutique"></div>
  <div class="hero-shade"></div>
  <div class="abs brand" style="left:78px;top:25px"><span class="brand-dot"></span>Corvell Ashdown</div>
  <nav class="abs nav"><span class="active">Home</span><span>About Us</span><span>Pick Up &amp; Delivery</span><span>Services</span><span>Contact Us</span></nav>
  <div class="abs login">
    <svg width="12" height="12" viewBox="0 0 12 12"><circle cx="6" cy="3.5" r="2.7" fill="#fff"/><path d="M1 12c0-3 2.2-5 5-5s5 2 5 5z" fill="#fff"/></svg>Login
  </div>
  <div class="btn" style="left:994px;top:36px;width:124px;height:34px;font-size:13px">Schedule Pick-up</div>
  <div class="abs center hero-kicker">Corvell Ashdown</div>
  <h1 class="abs center hero-title">Dry Cleaning &amp; Garment Experts</h1>
  <div class="abs zip"><span>Enter Your Zip Code ...</span><b>Get Started</b></div>
  <div class="abs center hero-note">We serving by MN</div>
  <div class="abs app-badge" style="left:410px"></div>
  <div class="abs app-badge" style="left:606px"></div>
</header>

<section class="why">
  <div class="abs center eyebrow" style="top:76px">Why Choose Us</div>
  <h2 class="abs center heading" style="top:104px">Corvell Ashdown</h2>
  <div class="feature" style="left:146px">
    <div class="feature-icon"><svg width="46" height="34" viewBox="0 0 46 34"><rect x="2" y="6" width="26" height="18" rx="2" fill="none" stroke="#85cae6" stroke-width="3"/><path d="M28 12h9l6 7v5H28z" fill="none" stroke="#85cae6" stroke-width="3"/><circle cx="11" cy="27" r="4" fill="#fff" stroke="#85cae6" stroke-width="3"/><circle cx="35" cy="27" r="4" fill="#fff" stroke="#85cae6" stroke-width="3"/></svg></div>
    <p>Free Pick Up &amp; Delivery</p>
  </div>
  <div class="feature" style="left:449px">
    <div class="feature-icon on"><svg width="40" height="40" viewBox="0 0 40 40"><path d="M8 21l8 8 16-17" fill="none" stroke="#fff" stroke-width="5" stroke-linecap="round" stroke-linejoin="round"/></svg></div>
    <p class="linked">Unmatched Quality</p>
  </div>
  <div class="feature" style="left:754px">
    <div class="feature-icon"><svg width="40" height="40" viewBox="0 0 40 40"><rect x="6" y="16" width="28" height="20" fill="none" stroke="#85cae6" stroke-width="3"/><rect x="3" y="10" width="34" height="7" fill="none" stroke="#85cae6" stroke-width="3"/><path d="M20 10v26" stroke="#85cae6" stroke-width="3"/></svg></div>
    <p>Toxin-Free Dry Cleaning</p>
  </div>
  <div class="btn-ghost" style="left:536px;top:354px;width:128px;height:32px">Sign up Here!</div>
</section>

<section class="about">
  <div class="abs eyebrow" style="left:157px;top:58px">Discover</div>
  <h2 class="abs heading" style="left:157px;top:84px;font-size:36px">About Us</h2>
  <p class="abs about-text" style="top:144px">Our passion started well over 50 years ago with our original store 'Brightwell' which was located in the heart of Downtown Lakeview, where Market Row stands today. We have now been in Lakeview for over 36 years! We are a family owned and operated business that provides quality and exceptional service. We take pride in our work and it shows!</p>
  <div class="btn" style="left:157px;top:264px;width:128px;height:32px;font-size:12px">Discover More</div>
  <div class="abs about-photo" role="img" aria-label="Colourful shirts on hangers along a clothing rail"></div>
</section>

<section class="services">
  <div class="abs center eyebrow" style="top:76px">What We Do</div>
  <h2 class="abs center heading" style="top:104px">Our Services</h2>
  <div class="arrow" style="left:120px;top:262px">&#8249;</div>
  <div class="service" style="left:155px"><div class="service-photo" role="img" aria-label="Dark suit with patterned tie" style="background:linear-gradient(135deg,#2a2c31,#55575c 50%,#1c1d21)"></div><p>Dry Cleaning</p></div>
  <div class="service" style="left:384px"><div class="service-photo" role="img" aria-label="Folded lavender dress shirt" style="background:linear-gradient(135deg,#9aa0c6,#7a80ad 50%,#b2b5d2)"></div><p class="linked">Shirt Laundering</p></div>
  <div class="service" style="left:610px"><div class="service-photo" role="img" aria-label="Tan suede jacket" style="background:linear-gradient(135deg,#8a5a2a,#b27a3e 50%,#6e4520)"></div><p>Suede &amp; Leather</p></div>
  <div class="service" style="left:839px"><div class="service-photo" role="img" aria-label="Stack of white folded towels" style="background:linear-gradient(135deg,#c9cdd2,#eef0f2 50%,#9aa2ab)"></div><p>Wash &amp; Fold</p></div>
  <div class="arrow" style="left:1064px;top:262px">&#8250;</div>
  <div class="btn-ghost" style="left:529px;top:456px;width:144px;height:32px;font-size:12px">View All Services</div>
</section>

<section class="guarantee">
  <div class="guarantee-photo" role="img" aria-label="Two smiling friends riding bicycles along a seaside boardwalk"></div>
  <svg class="abs" style="left:157px;top:62px" width="44" height="44" viewBox="0 0 44 44"><circle cx="22" cy="22" r="20" fill="#85abd2"/><circle cx="22" cy="22" r="13" fill="none" stroke="#fff" stroke-width="2"/><path d="M15 22l5 5 9-10" fill="none" stroke="#fff" stroke-width="3" stroke-linecap="round"/></svg>
  <h2 class="abs guarantee-title"><em>100%</em> Satisfaction Guarantee</h2>
  <p class="abs guarantee-text">If you're ever unhappy with the quality of our dry cleaning or pressing, we'll redo the item for free!</p>
  <div class="btn" style="left:157px;top:260px;width:128px;height:32px;font-size:12px">Contact Us</div>
</section>

<section class="testimonials">
  <div class="abs center eyebrow" style="top:76px">Testimonials</div>
  <h2 class="abs center heading" style="top:104px">What Our Clients Say</h2>
  <div class="arrow" style="left:84px;top:318px">&#8249;</div>
  <div class="quote" style="left:155px"><div class="avatar" role="img" aria-label="Client portrait"></div><p>"There are many variations of passages of Lorem Ipsum available, but the majority have suffered alteration in some form, by injected humour.</p><div class="who">Standard Chunk</div><div class="role">Accompanied</div></div>
  <div class="quote" style="left:460px"><div class="avatar" role="img" aria-label="Client portrait"></div><p>"There are many variations of passages of Lorem Ipsum available, but the majority have suffered alteration in some form, by injected humour.</p><div class="who">Standard Chunk</div><div class="role">Accompanied</div></div>
  <div class="quote" style="left:765px"><div class="avatar" role="img" aria-label="Client portrait"></div><p>"There are many variations of passages of Lorem Ipsum available, but the majority have suffered alteration in some form, by injected humour.</p><div class="who">Standard Chunk</div><div class="role">Accompanied</div></div>
  <div class="arrow" style="left:1034px;top:318px">&#8250;</div>
</section>

<footer class="site-footer">
  <div class="abs brand" style="left:157px;top:70px"><span class="brand-dot" style="width:50px;height:50px"></span>Corvell Ashdown</div>
  <div class="abs" style="left:157px;top:148px;font-size:17px;color:var(--accent);display:flex;align-items:center;gap:6px">Call Us:
    <svg width="14" height="14" viewBox="0 0 14 14"><path d="M3 1l3 3-1.5 1.8a8 8 0 0 0 3.7 3.7L10 8l3 3-2 2C6 13 1 8 1 3z" fill="#85cae6"/></svg>
    <span style="color:#fff">(555) 014-7720</span></div>
  <div class="abs" style="left:157px;top:178px;font-size:13px;color:#fff;text-decoration:underline">info@corvellashdowncleaners.example</div>
  <div class="abs" style="left:157px;top:216px;font-size:12px;line-height:16px">218 Harrow Lane, Lakeview,<br>MN 55000</div>
  <div class="abs" style="left:157px;top:262px;font-size:13px;color:var(--accent);text-decoration:underline">Get Directions</div>
  <div class="footer-col" style="left:536px"><h4>Our Services</h4>Dry Cleaning<br>Shirt Laundering<br>Suede &amp; Leather<br>Wash &amp; Fold<br>Wedding &amp; Formal Gowns<br>Table &amp; Bed Linens<br>Area Rugs<br>Alterations</div>
  <div class="footer-col" style="left:765px"><h4>Quick Links</h4><span class="current">Home</span><br>About Us<br>Pick Up &amp; Delivery<br>Services<br>Terms and Conditions<br>Privacy Policy<br>Contact Us</div>
  <div class="social" style="top:98px"></div>
  <div class="social on" style="top:147px"></div>
  <div class="social" style="top:197px"></div>
  <div class="social" style="top:246px"></div>
  <div class="abs rule"></div>
  <div class="abs" style="left:157px;top:400px;font-size:12px">© 2018 <span style="color:var(--accent)">Corvell Ashdown Dry Cleaners</span>. All Right Reserved.</div>
  <div class="abs" style="left:765px;top:387px;width:125px;height:45px;background:#2a5d86;border-radius:2px"></div>
  <div class="abs" style="left:1003px;top:387px;width:40px;height:40px;border-radius:50%;background:var(--accent-deep);display:flex;align-items:center;justify-content:center">
    <svg width="14" height="10" viewBox="0 0 14 10"><path d="M2 8l5-5 5 5" fill="none" stroke="#fff" stroke-width="2"/></svg>
  </div>
</footer>

</body>
</html>
```